Business Card Design for Business Broker

Hi - I am looking for a cool design for my new business card using the logo attached.

We are business brokers. We help people buy and sell businesses!

I am open to just about anything. As far as colors, I do like the navy blue that is part of my logo.

Industry/Entity Type

Business

```html
<!DOCTYPE html>
<html lang="en">
<head>
<meta charset="utf-8">
<title>Business Card – Front and Back</title>
<link rel="stylesheet" href="https://fonts.googleapis.com/css2?family=Arimo:wght@400&display=swap">
<style>
  :root {
    --navy: #0c1f63;
    --white: #ffffff;
    --grey-text: #6b6b6b;
    --rule: #c9c9c9;
    --sans: "Arimo", Arial, sans-serif;
  }
  html, body {
    margin: 0;
    padding: 0;
    width: 1200px;
    height: 301px;
    overflow: hidden;
    background: var(--white);
  }
  .sheet {
    position: relative;
    width: 1200px;
    height: 301px;
  }
  .card {
    position: absolute;
    top: 0;
    height: 301px;
    background: var(--white);
    overflow: hidden;
  }
  .card--front { left: 0; width: 593px; }
  .card--back { left: 605px; width: 595px; }

  .band-top {
    position: absolute;
    left: 0; top: 0;
    width: 100%;
    height: 7px;
    background: var(--navy);
  }
  .band-bottom {
    position: absolute;
    left: 0; bottom: 0;
    width: 100%;
    height: 12px;
    background: var(--navy);
  }

  .contact {
    position: absolute;
    top: 20px;
    margin: 0;
    font-family: var(--sans);
    font-size: 16px;
    color: var(--grey-text);
  }
  .contact--phone { left: 3px; }
  .contact--email { right: 5px; }

  .person__name {
    position: absolute;
    left: 0; width: 100%;
    top: 137px;
    margin: 0;
    font-family: var(--sans);
    font-weight: 400;
    font-size: 64px;
    line-height: 1;
    letter-spacing: 1px;
    text-align: center;
    color: var(--navy);
  }
  .person__rule {
    position: absolute;
    left: 140px;
    width: 316px;
    height: 1px;
    background: var(--rule);
  }
  .person__rule--upper { top: 210px; }
  .person__rule--lower { top: 251px; }
  .person__role {
    position: absolute;
    left: 0; width: 100%;
    top: 215px;
    margin: 0;
    font-family: var(--sans);
    font-size: 18px;
    text-align: center;
    color: var(--grey-text);
  }

  .brand__name {
    position: absolute;
    left: 0; width: 100%;
    top: 84px;
    margin: 0;
    font-family: var(--sans);
    font-weight: 400;
    font-size: 78px;
    line-height: 1;
    letter-spacing: 2px;
    text-align: center;
    color: var(--navy);
  }
  .brand__tagline {
    position: absolute;
    left: 0; width: 100%;
    top: 163px;
    margin: 0;
    font-family: var(--sans);
    font-weight: 400;
    font-size: 32px;
    line-height: 1;
    letter-spacing: 0.5px;
    text-align: center;
    color: var(--navy);
  }
  .brand__rule {
    position: absolute;
    left: 40px;
    width: 515px;
    top: 205px;
    height: 1px;
    background: var(--rule);
  }

  .office {
    position: absolute;
    left: 0; bottom: 0;
    width: 100%;
    height: 73px;
    background: var(--navy);
    color: var(--white);
    font-family: var(--sans);
    text-align: center;
  }
  .office p { margin: 0; line-height: 1.15; }
  .office__label { font-size: 19px; padding-top: 3px; }
  .office__address,
  .office__web { font-size: 14px; margin-top: 2px !important; }
</style>
</head>
<body>
  <main class="sheet">
    <section class="card card--front" aria-label="Card front">
      <div class="band-top"></div>
      <p class="contact contact--phone">+xx xx xxxxx xxxx</p>
      <p class="contact contact--email">abc@xyz.com</p>
      <h1 class="person__name">XYZ ABCD</h1>
      <div class="person__rule person__rule--upper"></div>
      <p class="person__role">Designation</p>
      <div class="person__rule person__rule--lower"></div>
      <div class="band-bottom"></div>
    </section>

    <section class="card card--back" aria-label="Card back">
      <div class="band-top"></div>
      <h2 class="brand__name">MarlowKent</h2>
      <p class="brand__tagline">Business Brokers &amp; Consultants</p>
      <div class="brand__rule"></div>
      <div class="office">
        <p class="office__label">Address</p>
        <p class="office__address">OFC Address</p>
        <p class="office__web">www.abc.com</p>
      </div>
    </section>
  </main>
</body>
</html>
```